business card and stationary pest control company
Bugwarden
business card and stationary pest control company - Cleaning
Creative Brief
Bright & Fun-filled
Malcolm Teague
General Manager
to be added
info@bugwarden.example
bugwarden.example
tarloq tarloq
Hi guys, please bear in mind it's a full stationary project, letterhead, fax, email, envelope etc ...
ravenmoss ravenmoss
check your private messages on top right! thankyou

```html
<!DOCTYPE html>
<html lang="en">
<head>
<meta charset="utf-8">
<title>Bugwarden – Business Card</title>
<link rel="stylesheet" href="https://fonts.googleapis.com/css2?family=Arimo:wght@400;700&display=swap">
<style>
  :root {
    --brand-blue: #12389a;
    --brand-red: #e3201f;
    --paper: #ffffff;
    --ink-grey: #8a8f99;
    --backdrop: #e9e9eb;
  }
  * { box-sizing: border-box; margin: 0; padding: 0; }
  html, body { width: 1200px; height: 778px; overflow: hidden; }
  body {
    background: var(--backdrop);
    font-family: "Arimo", Arial, sans-serif;
    position: relative;
  }
  .side-label {
    position: absolute;
    font-size: 15px;
    font-style: italic;
    color: #555;
  }
  .side-label--front { left: 40px; top: 86px; }
  .side-label--back { left: 620px; top: 666px; }

  .card {
    position: absolute;
    width: 540px;
    height: 312px;
    overflow: hidden;
    box-shadow: 0 6px 18px rgba(0,0,0,.18);
  }

  /* Front */
  .card--front { left: 40px; top: 112px; background: var(--paper); }
  .brand {
    position: absolute;
    left: 30px;
    top: 66px;
    color: var(--brand-blue);
  }
  .brand__name {
    font-size: 42px;
    font-weight: 700;
    letter-spacing: -1.5px;
    line-height: 1;
  }
  .brand__tagline {
    font-size: 16px;
    margin-top: 2px;
    letter-spacing: .2px;
  }
  .person {
    position: absolute;
    right: 40px;
    top: 74px;
    text-align: right;
  }
  .person__name { color: var(--brand-blue); font-size: 18px; }
  .person__role { color: var(--brand-red); font-size: 12px; margin-top: 2px; }

  .front-band { position: absolute; left: 0; top: 0; }
  .contact {
    position: absolute;
    left: 30px;
    top: 200px;
    color: var(--paper);
    font-size: 13px;
    line-height: 19px;
  }
  .contact__email { display: flex; align-items: center; gap: 6px; margin-top: 10px; }
  .website {
    position: absolute;
    left: 30px;
    bottom: 10px;
    color: var(--ink-grey);
    font-size: 13px;
  }

  /* Back */
  .card--back { left: 620px; top: 350px; background: var(--brand-blue); }
  .back-art { position: absolute; left: 0; top: 0; }
  .back-brand {
    position: absolute;
    right: 22px;
    bottom: 22px;
    color: var(--paper);
  }
  .back-brand .brand__name { font-size: 40px; }
  .back-brand .brand__tagline { font-size: 15px; }
</style>
</head>
<body>
  <span class="side-label side-label--front">Front</span>

  <section class="card card--front">
    <svg class="front-band" width="540" height="312" viewBox="0 0 540 312" aria-hidden="true">
      <polygon points="0,178 300,178 340,150 540,150 540,268 0,268" fill="var(--brand-blue)"/>
    </svg>

    <div class="brand">
      <div class="brand__name">Bugwarden</div>
      <div class="brand__tagline">discreet pest control</div>
    </div>

    <div class="person">
      <div class="person__name">Malcolm Teague</div>
      <div class="person__role">General Manager</div>
    </div>

    <div class="contact">
      <div>P.O.BOX 00000</div>
      <div>Area Country etc.</div>
      <div class="contact__email">
        <svg width="12" height="9" viewBox="0 0 12 9" aria-hidden="true">
          <rect x="0.5" y="0.5" width="11" height="8" fill="none" stroke="#fff"/>
          <polyline points="0.5,0.5 6,5 11.5,0.5" fill="none" stroke="#fff"/>
        </svg>
        <span>info@bugwarden.example</span>
      </div>
    </div>

    <div class="website">www.bugwarden.example</div>
  </section>

  <section class="card card--back">
    <svg class="back-art" width="540" height="312" viewBox="0 0 540 312" aria-hidden="true">
      <polygon points="0,0 130,0 0,110" fill="var(--brand-red)"/>
      <polygon points="130,0 175,0 0,148 0,110" fill="var(--paper)"/>
    </svg>
    <div class="back-brand">
      <div class="brand__name">Bugwarden</div>
      <div class="brand__tagline">discreet pest control</div>
    </div>
  </section>

  <span class="side-label side-label--back">Back</span>
</body>
</html>
```